The Lindenmoor Compass Book

Cover Design for my first book. The book is for elementary school principals who are unhappy and are considering a career change but are afraid to leave. I teach them how to develop emotional fitness and resiliency through thought management so that they can decide whether to stay or leave their position from a place of empowerment. I've attached my podcast artwork for your reference. My publisher suggested not having me on the cover which is fine. I just thought it might be helpful.

Target Market(s)

Elementary School Principals

Industry/Entity Type

Education

Logo Text

The Lindenmoor Compass

Font styles to use
Serif
Sans Serif

Colors
34a6d7
33b8a4
3276b5

Requirements
Must have
• Title, Author name, photo or artwork that captures the essence of the book

```html
<!DOCTYPE html>
<html lang="en">
<head>
<meta charset="utf-8">
<title>The Lindenmoor Compass – Cover</title>
<link href="https://fonts.googleapis.com/css2?family=Montserrat:wght@300;400;900&family=Oswald:wght@500;600&display=swap" rel="stylesheet">
<style>
  :root {
    --stage: #545454;
    --paper: #f7f7f7;
    --ink: #111111;
    --blue: #3276b5;
    --sky: #34a6d7;
    --teal: #33b8a4;
    --violet: #5b44a8;
    --indigo: #2f2a74;
    --crimson: #8c1426;
    --plum: #24122e;
    --subtitle: #2a2766;
    --white: #ffffff;
  }
  * { margin: 0; padding: 0; box-sizing: border-box; }
  html, body { width: 1198px; height: 1200px; overflow: hidden; background: var(--stage); }
  .cover {
    position: absolute; left: 141px; top: 0;
    width: 916px; height: 1200px;
    background: var(--paper);
    overflow: hidden;
  }
  .cover-art {
    position: absolute; left: 225px; top: 70px;
    width: 730px; height: 1150px;
    border-radius: 48% 42% 0 0 / 24% 20% 0 0;
    background:
      radial-gradient(ellipse at 50% 10%, var(--crimson) 0%, rgba(140,20,38,0) 40%),
      radial-gradient(ellipse at 75% 50%, var(--teal) 0%, rgba(51,184,164,0) 34%),
      radial-gradient(ellipse at 20% 72%, var(--sky) 0%, rgba(52,166,215,0) 38%),
      radial-gradient(ellipse at 55% 95%, var(--crimson) 0%, rgba(140,20,38,0) 35%),
      linear-gradient(180deg, #5a2a6a 0%, var(--violet) 35%, var(--blue) 65%, #4a3a8c 100%);
    opacity: .9;
  }
  .title { position: absolute; left: 0; top: 0; width: 100%; font-family: 'Montserrat', sans-serif; font-weight: 400; }
  .title-article {
    position: absolute; left: 76px; top: 173px;
    font-weight: 300; font-size: 128px; line-height: 1; color: var(--ink);
  }
  .title-block {
    position: absolute; left: 70px;
    font-weight: 900; line-height: 1; letter-spacing: -0.04em;
    background: linear-gradient(100deg, var(--blue) 0%, var(--violet) 30%, var(--crimson) 55%, var(--plum) 78%);
    -webkit-background-clip: text; background-clip: text; color: transparent;
    opacity: .92;
  }
  .title-block--one { top: 244px; font-size: 330px; }
  .title-block--two { top: 508px; font-size: 330px; }
  .title-block--three { top: 846px; font-size: 150px; left: 72px; }
  .title-sub {
    position: absolute; left: 84px; top: 985px;
    font-weight: 400; font-size: 64px; line-height: 1; letter-spacing: 0.42em;
    color: var(--subtitle);
  }
  .author {
    position: absolute; left: 262px; top: 1104px;
    font-family: 'Oswald', sans-serif; font-weight: 600; font-size: 35px;
    color: var(--white); letter-spacing: 0.01em; line-height: 1.2;
    white-space: nowrap;
  }
  .author-lead { font-weight: 500; font-size: 27px; margin-right: 8px; }
</style>
</head>
<body>
  <main class="cover">
    <div class="cover-art" role="img" aria-label="Painted portrait artwork of a woman seen from behind, glancing over her shoulder, in violet, blue, teal and red brushstrokes"></div>
    <h1 class="title">
      <span class="title-article">THE</span>
      <span class="title-block title-block--one">LIN</span>
      <span class="title-block title-block--two">DEN</span>
      <span class="title-block title-block--three">MOOR</span>
      <span class="title-sub">COMPASS</span>
    </h1>
    <p class="author"><span class="author-lead">WITH</span>MARION HALE DORSEY</p>
  </main>
</body>
</html>
```